Corvella Foundation is a new grant making charity set up in the UK.

Having got a logo, we now need a website to go with it. We have worked out the text which people are going to need in order to then apply for grants. But having found out what we require they will probably need to go away and think about it.
We have to be careful of what images we use. So I have uploaded some images that we like. We are also going to be adding more pages almost immediately so need to think about the images for these.
I know basic wordpress so I will be able to add new pages/make alterations in future.
Updates
The website does need to be coded in Wordpress so that I can maintain it afterwards.
Marisse
Brief changed to provide more money and we have also provided more possible pictures. And generally more explanation.
Target Market(s)
departments in universities, other charities doing work on relief of pain, people working in health service departments
Industry/Entity Type
Health Charity
Coding
Coded - Design and coding required
Number of Pages Required
4 page
Look and feel
Each slider illustrates characteristics of the customer's brand and the style your logo design should communicate.

```html
<!DOCTYPE html>
<html lang="en">
<head>
<meta charset="utf-8">
<title>Corvella Foundation</title>
<link rel="stylesheet" href="https://fonts.googleapis.com/css2?family=Montserrat:wght@500;600;700&family=Roboto:wght@400;500;700&display=swap">
<style>
:root{
  --blue:#0e6fc0;
  --blue-dark:#0a58a0;
  --grant-blue:#1f7bd0;
  --ink:#111;
  --body:#555;
  --line:#9a9a9a;
  --black:#000;
  --white:#fff;
}
*{margin:0;padding:0;box-sizing:border-box}
html,body{width:1200px;height:3702px;overflow:hidden;background:var(--white)}
body{font-family:"Roboto",sans-serif;color:var(--ink);position:relative}
.abs{position:absolute}
.heading{font-family:"Montserrat",sans-serif;font-weight:700;letter-spacing:.5px}

/* header */
.site-header{position:absolute;top:0;left:0;width:1200px;height:96px;border-top:4px solid var(--blue);background:var(--white)}
.site-header .notch{position:absolute;left:735px;top:0;width:0;height:0;border-left:9px solid transparent;border-right:9px solid transparent;border-top:14px solid var(--blue)}
.brand{position:absolute;left:112px;top:29px;display:flex;align-items:center;gap:10px}
.brand-mark{width:30px;height:30px;background:var(--blue)}
.brand-name{font-family:"Roboto",sans-serif;font-weight:700;font-size:22px;color:var(--blue);letter-spacing:.3px}
.main-nav{position:absolute;right:114px;top:40px;display:flex;gap:31px;font-size:14px;font-weight:500}
.main-nav a{color:var(--ink);text-decoration:none}
.main-nav a.current{color:var(--blue);border-bottom:2px solid var(--blue);padding-bottom:4px}

/* hero */
.hero{position:absolute;top:96px;left:0;width:1200px;height:646px;background:radial-gradient(ellipse at 72% 40%,#3c7fc8 0%,#15408a 35%,#0a2358 70%,#061531 100%)}
.hero h1{position:absolute;left:112px;top:164px;font-size:43px;line-height:51px;color:var(--white);text-transform:uppercase}
.hero .btn{position:absolute;left:112px;top:387px;width:154px;height:50px;background:var(--white);color:var(--blue);font-size:14px;font-weight:500;display:flex;align-items:center;justify-content:center}
.hero .dots{position:absolute;left:576px;top:569px;display:flex;gap:5px}
.hero .dots span{width:13px;height:13px;border-radius:50%;background:var(--white)}
.hero .dots span.on{background:var(--blue)}
.hero-cut{position:absolute;top:716px;left:0}

/* about */
.about-title{position:absolute;top:836px;width:1200px;text-align:center;font-size:35px}
.faq{position:absolute;left:112px;width:488px}
.faq .num{position:absolute;left:0;top:2px;width:34px;height:34px;border-radius:50%;background:var(--blue);color:var(--white);font-size:15px;font-weight:500;display:flex;align-items:center;justify-content:center}
.faq h3{margin-left:47px;font-size:16.5px;font-weight:500;color:var(--blue);line-height:22px}
.faq p{margin-left:47px;margin-top:12px;font-size:13px;line-height:22px;color:var(--body)}
.about-photo{position:absolute;left:621px;width:465px}
.photo-top{top:925px;height:273px;background:radial-gradient(ellipse at 40% 50%,#4d8fd6 0%,#1a4d98 45%,#0b2458 100%)}
.photo-bottom{top:1216px;height:360px;background:linear-gradient(135deg,#a9c6d8 0%,#b9cfdc 50%,#c89a80 100%)}
.photo-badge{position:absolute;left:736px;top:1162px;width:235px;height:93px;background:#dbe9f7;border:4px solid var(--white);display:flex;align-items:center;justify-content:center;gap:8px}
.photo-badge .brand-mark{width:26px;height:26px}
.photo-badge .brand-name{font-size:19px}

/* grants */
.grants{position:absolute;top:1681px;left:0;width:1200px;height:693px;background:linear-gradient(180deg,var(--grant-blue) 0%,#1a72c6 60%,#1468b8 100%)}
.grants-art{position:absolute;left:112px;top:104px;width:463px;height:478px;background:radial-gradient(ellipse at 50% 50%,#fbfdd8 0%,#f4fc9e 70%)}
.grants-body{position:absolute;left:615px;top:112px;width:480px;color:var(--white)}
.grants-body h2{font-size:33px;margin-bottom:24px}
.grants-body p{font-size:13px;line-height:21.5px;margin-bottom:21px}
.grants-body h4{font-size:15px;font-weight:700;line-height:26px;margin-bottom:18px}
.grants-body ul{list-style:none}
.grants-body li{font-size:13px;display:flex;align-items:center;gap:12px;height:30px}

/* contact */
.contact-title{position:absolute;top:2470px;width:1200px;text-align:center;font-size:44px}
.contact-sub{position:absolute;top:2515px;width:1200px;text-align:center;font-size:13px;color:#f2f2f2}
.info{position:absolute;top:2555px;width:240px;text-align:center;font-size:13px;line-height:20px}
.info svg{display:block;margin:0 auto 10px}
.info b{font-weight:500;display:block}
.field{position:absolute;border:1px solid var(--line);background:var(--white);font-size:13px;color:#666;padding:0 22px;display:flex;align-items:center}
.field.area{align-items:flex-start;padding-top:22px}
.submit{position:absolute;left:521px;top:3026px;width:159px;height:48px;border-radius:24px;background:var(--blue);color:var(--white);font-size:14px;font-weight:700;display:flex;align-items:center;justify-content:center}

/* footer */
.site-footer{position:absolute;top:3177px;left:0;width:1200px;height:525px;background:var(--black);color:var(--white)}
.subscribe{position:absolute;left:374px;top:125px;width:452px;height:42px;border-radius:21px;background:var(--white);border:2px solid var(--blue)}
.subscribe span{position:absolute;left:34px;top:12px;font-size:13px;color:#666}
.subscribe b{position:absolute;right:-2px;top:-2px;width:152px;height:42px;border-radius:21px;background:var(--blue);font-size:13px;display:flex;align-items:center;justify-content:center}
.foot-col h5{font-family:"Montserrat",sans-serif;font-weight:600;font-size:22px;margin-bottom:16px}
.foot-col{position:absolute;top:226px;font-family:"Montserrat",sans-serif;font-size:14.5px}
.foot-col li{list-style:none;line-height:28.5px}
.contact-line{display:flex;gap:14px;line-height:28.5px}
.contact-line svg{margin-top:9px;flex:none}
.divider{position:absolute;top:233px;width:1px;height:150px;background:#777}
.social{display:flex;gap:8px}
.social span{width:37px;height:37px;border-radius:50%;border:1.5px solid var(--white)}
.copyright{position:absolute;top:453px;width:1200px;text-align:center;font-family:"Montserrat",sans-serif;font-size:14px}
</style>
</head>
<body>

<header class="site-header">
  <span class="notch"></span>
  <div class="brand"><span class="brand-mark"></span><span class="brand-name">Corvella Foundation</span></div>
  <nav class="main-nav">
    <a class="current" href="#">HOME</a>
    <a href="#">ABOUT US</a>
    <a href="#">GRANTS</a>
    <a href="#">CONTACT US</a>
  </nav>
</header>

<section class="hero" role="img" aria-label="Close-up illustration of glowing blue nerve cells and neural connections">
  <h1 class="heading">The main aim of Corvella<br>Foundation is to reduce<br>the suffering caused<br>by chronic pain</h1>
  <span class="btn">GET STARTED</span>
  <div class="dots"><span></span><span class="on"></span><span></span></div>
</section>
<svg class="hero-cut" width="1200" height="26" viewBox="0 0 1200 26">
  <polygon points="0,0 430,0 470,26 0,26" fill="#fff"/>
  <polygon points="430,0 460,0 495,26 470,26" fill="#0e6fc0"/>
</svg>

<h2 class="heading about-title">ABOUT CORVELLA FOUNDATION</h2>

<div class="faq" style="top:925px"><span class="num">1</span>
  <h3>Who are the trustees of Corvella Foundation?</h3>
  <p>The initial trustees are Marisse, Peter &amp; Adrian Velloran.<br>A fourth trustee is about to be appointed, the legal firm of Harwood Lyle.</p></div>
<div class="faq" style="top:1030px"><span class="num">2</span>
  <h3>Who are the medical advisers to Corvella Foundation?</h3>
  <p>The medical advisers are doctors or other health professionals, who individually or collectively advise the trustees on the merit of grant applications. Medical advisers are initially appointed for a five year term.</p></div>
<div class="faq" style="top:1178px"><span class="num">3</span>
  <h3>How much money does Corvella Foundation have?</h3>
  <p>It is unclear how much money the Foundation will have in a few years time, but currently it has about a million pounds.</p></div>
<div class="faq" style="top:1283px"><span class="num">4</span>
  <h3>Where has this money come from?</h3>
  <p>The million pounds has been inherited from Marisse’s father, the late Sir Edmund Ashcombe, who had a large stake in the Ashcombe supermarket business. Further significant money is going to come from the sale of the farm where the Velloran family currently live.</p></div>
<div class="faq" style="top:1431px"><span class="num">5</span>
  <h3>Why is the foundation named after Marisse Velloran?</h3>
  <p>Marisse Velloran suffered from extreme pain for many years after a successful operation to cure her cancer of the tongue. Although the pain is now well controlled, the family would like the unexpected receipt of such a large amount of money from the farm, to help prevent other people going through such a difficult time.</p></div>

<div class="about-photo photo-top" role="img" aria-label="Illustration of a glowing blue neuron"></div>
<div class="about-photo photo-bottom" role="img" aria-label="Photo of an open hand holding round paper cards showing different moods"></div>
<div class="photo-badge"><span class="brand-mark"></span><span class="brand-name">Corvella Foundation</span></div>

<section class="grants">
  <div class="grants-art" role="img" aria-label="Word cloud of pain-related words on a pale yellow background"></div>
  <div class="grants-body">
    <h2 class="heading">GRANTS</h2>
    <p>Grants will almost entirely be provided for research or education into pain management, or the prevention of pain.</p>
    <p>The trustees will also be providing grants to a number of other charities or to areas with which they have had a long term association, such as HIV/AIDS and TB. There is no application procedure for these other areas, and unsolicited applications are unlikely to be favorably considered by the trustees</p>
    <h4>The main categories of funding for pain research or<br>education will be as follows.</h4>
    <ul>
      <li><svg width="13" height="13" viewBox="0 0 13 13"><circle cx="6.5" cy="6.5" r="6.5" fill="#fff"/><path d="M3.5 6.7l2 2 4-4" stroke="#1f7bd0" stroke-width="1.8" fill="none"/></svg>Pain centres</li>
      <li><svg width="13" height="13" viewBox="0 0 13 13"><circle cx="6.5" cy="6.5" r="6.5" fill="#fff"/><path d="M3.5 6.7l2 2 4-4" stroke="#1f7bd0" stroke-width="1.8" fill="none"/></svg>The use of opioids</li>
      <li><svg width="13" height="13" viewBox="0 0 13 13"><circle cx="6.5" cy="6.5" r="6.5" fill="#fff"/><path d="M3.5 6.7l2 2 4-4" stroke="#1f7bd0" stroke-width="1.8" fill="none"/></svg>Improving the use of medication</li>
      <li><svg width="13" height="13" viewBox="0 0 13 13"><circle cx="6.5" cy="6.5" r="6.5" fill="#fff"/><path d="M3.5 6.7l2 2 4-4" stroke="#1f7bd0" stroke-width="1.8" fill="none"/></svg>Education</li>
      <li><svg width="13" height="13" viewBox="0 0 13 13"><circle cx="6.5" cy="6.5" r="6.5" fill="#fff"/><path d="M3.5 6.7l2 2 4-4" stroke="#1f7bd0" stroke-width="1.8" fill="none"/></svg>Improved types of pain control</li>
      <li><svg width="13" height="13" viewBox="0 0 13 13"><circle cx="6.5" cy="6.5" r="6.5" fill="#fff"/><path d="M3.5 6.7l2 2 4-4" stroke="#1f7bd0" stroke-width="1.8" fill="none"/></svg>Measuring pain</li>
    </ul>
  </div>
</section>

<h2 class="heading contact-title">GET IN TOUCH</h2>
<p class="contact-sub">Lorem ipsum dolor sit amet, consectetur adipiscing elit, sed do eiusmod</p>

<div class="info" style="left:248px">
  <svg width="64" height="64" viewBox="0 0 64 64"><circle cx="32" cy="32" r="30.5" fill="none" stroke="#111" stroke-width="2"/><path d="M32 20a8 8 0 0 0-8 8c0 6 8 15 8 15s8-9 8-15a8 8 0 0 0-8-8z" fill="#0e6fc0"/><circle cx="32" cy="28" r="3" fill="#fff"/></svg>
  <b>ADDRESS :</b>Address: 48 Linden Row, Suite 12,<br>Leeds LS1 4AP</div>
<div class="info" style="left:488px">
  <svg width="64" height="64" viewBox="0 0 64 64"><circle cx="32" cy="32" r="30.5" fill="none" stroke="#111" stroke-width="2"/><path d="M25 22l4-1 3 6-3 2c1 3 4 6 7 7l2-3 6 3-1 4c-10 1-19-8-18-18z" fill="#0e6fc0"/></svg>
  <b>PHONE :</b>0113 496 0400</div>
<div class="info" style="left:726px">
  <svg width="64" height="64" viewBox="0 0 64 64"><circle cx="32" cy="32" r="30.5" fill="none" stroke="#111" stroke-width="2"/><rect x="20" y="24" width="24" height="17" rx="2" fill="#0e6fc0"/><path d="M20 26l12 8 12-8" stroke="#fff" stroke-width="2" fill="none"/></svg>
  <b>EMAIL :</b>info@corvellafdn.org</div>

<div class="field" style="left:238px;top:2716px;width:352px;height:57px">First name</div>
<div class="field" style="left:608px;top:2716px;width:351px;height:57px">Last name</div>
<div class="field" style="left:238px;top:2791px;width:352px;height:57px">Phone</div>
<div class="field" style="left:608px;top:2791px;width:351px;height:57px">Email address</div>
<div class="field area" style="left:238px;top:2868px;width:721px;height:134px">Message</div>
<span class="submit">SUBMIT</span>

<footer class="site-footer">
  <svg class="abs" style="top:0;left:0" width="1200" height="26" viewBox="0 0 1200 26">
    <polygon points="0,0 705,0 740,26 0,26" fill="#fff"/>
    <polygon points="705,0 740,0 770,26 740,26" fill="#0e6fc0"/>
    <rect x="0" y="0" width="1200" height="0" fill="#000"/>
  </svg>
  <div class="subscribe"><span>Email address</span><b>SUBSCRIBE</b></div>

  <div class="foot-col" style="left:138px"><h5>Links</h5>
    <ul><li>Home</li><li>Services</li><li>Blog</li><li>Contact</li></ul></div>
  <span class="divider" style="left:336px"></span>
  <div class="foot-col" style="left:461px;width:300px"><h5>Contact us</h5>
    <div class="contact-line"><svg width="10" height="12" viewBox="0 0 10 12"><path d="M5 0a5 5 0 0 0-5 5c0 3.5 5 7 5 7s5-3.5 5-7a5 5 0 0 0-5-5z" fill="#fff"/><circle cx="5" cy="5" r="1.8" fill="#000"/></svg><span>123,Lorem ipsum dolor sit amet,<br>consec</span></div>
    <div class="contact-line"><svg width="12" height="12" viewBox="0 0 12 12"><path d="M1 1l3-1 2 3-2 1.5c1 2 2.5 3.5 4.5 4.5L10 6l2 2-1 3C5 11 1 7 1 1z" fill="#fff"/></svg><span>+1 888 888 8888</span></div>
    <div class="contact-line"><svg width="12" height="10" viewBox="0 0 12 10"><rect width="12" height="10" rx="1" fill="#fff"/><path d="M0 1l6 4 6-4" stroke="#000" stroke-width="1.2" fill="none"/></svg><span>info@companyname.com</span></div>
  </div>
  <span class="divider" style="left:818px"></span>
  <div class="foot-col" style="left:898px"><h5 style="margin-left:46px">Follow us</h5>
    <div class="social"><span></span><span></span><span></span><span></span></div></div>

  <p class="copyright">© Copyrights.2021.The Company Name.All Rights Reserved</p>
</footer>

</body>
</html>
```